Informational Sales Documents For Digital Media Firm Offering Services To Restaurants and Nightlife

We need three documents designed into presentation decks (PDF Format) with info graphics. It can be as many pages as needed so long as it is visually captivating and legible along with good flow. The documents are attached.

We would like the documents to be in line with the look of our website. I am also providing examples of some work that we like that is in the direction that we want and here is a link with some pictures we have used as a company (no need to necessarily use them, more for guidance).

https://www.fileharbor.example/sh/k7rtm2wqpln84/ZZQeLm4Tn0Pb77r_-v9WkRtBb?dl=0

We are also attaching our logo.

the documents are to be used digitally so the exact size and orientation (landscape v. vertical) is up to you as the designer and for what is in line with the design you are envisioning for this project.

Target Market(s)

Restaurant, Nightclub, Lounge and Bar Owners

Industry/Entity Type

Hospitality

Font styles to use
Serif

Requirements
Must have
• All the text and data from the word files.
• Have a professional yet modern look in line with our website www.brightvellum.ca
• True Black and True White colour
Should not have
• Any colour (the color option is not working here so b&w only)
• Non-impactful images

```html
<!DOCTYPE html>
<html lang="en">
<head>
<meta charset="utf-8">
<title>Bright Vellum – What Is Bright Vellum</title>
<link rel="stylesheet" href="https://fonts.googleapis.com/css2?family=Questrial&family=Arimo:wght@700&display=swap">
<style>
  :root {
    --ink: #000000;
    --text: #2a2a2a;
    --muted: #6b6b6b;
    --rule: #9a9a9a;
    --paper: #ffffff;
    --backdrop: #ededed;
  }
  * { margin: 0; padding: 0; box-sizing: border-box; }
  html, body { width: 1200px; height: 1000px; overflow: hidden; background: var(--backdrop); }
  .page {
    position: absolute; left: 0; top: 77px;
    width: 1200px; height: 845px;
    background: var(--paper);
    font-family: "Questrial", sans-serif;
    color: var(--text);
  }
  .brand { position: absolute; left: 60px; top: 120px; width: 390px; text-align: center; }
  .brand-row { display: flex; align-items: center; justify-content: center; gap: 14px; }
  .brand-mark { width: 26px; height: 26px; border-radius: 50%; background: var(--ink); flex: none; }
  .brand-name { font-size: 34px; letter-spacing: 2px; color: var(--ink); line-height: 1; }
  .brand-tagline { margin-top: 14px; font-size: 14px; letter-spacing: 3.5px; color: var(--muted); }
  .hero-visual {
    position: absolute; left: 683px; top: 67px; width: 409px; height: 216px;
    background: linear-gradient(90deg, #e6e6e6 0%, #f3f3f3 55%, #fbfbfb 100%);
  }
  .section-head {
    position: absolute; left: 68px; top: 288px; right: 69px;
    display: flex; align-items: center; gap: 16px;
  }
  .section-head h2 { font-family: "Arimo", sans-serif; font-size: 14px; color: var(--ink); white-space: nowrap; }
  .section-head .rule { flex: 1; height: 1px; background: var(--rule); }
  .column {
    position: absolute; top: 330px; width: 311px;
    font-size: 13.6px; line-height: 19px; text-align: justify;
  }
  .column p + p { margin-top: 19px; }
  .col-one { left: 68px; }
  .col-two { left: 440px; }
  .divider { position: absolute; top: 320px; height: 340px; width: 1px; background: var(--muted); }
  .divider-a { left: 412px; }
  .divider-b { left: 787px; }
  .base-rule { position: absolute; left: 68px; top: 680px; width: 1057px; height: 1px; background: var(--rule); }
  .contact {
    position: absolute; left: 0; right: 0; top: 796px;
    display: flex; justify-content: center; align-items: center; gap: 8px;
    font-size: 8.5px; letter-spacing: 0.6px; color: var(--muted); text-transform: uppercase;
  }
  .contact .dot { width: 7px; height: 7px; border-radius: 50%; background: var(--muted); }
</style>
</head>
<body>
<main class="page">
  <div class="brand">
    <div class="brand-row">
      <span class="brand-mark"></span>
      <span class="brand-name">BRIGHT VELLUM</span>
    </div>
    <div class="brand-tagline">HOSPITALITY MADE SOCIAL</div>
  </div>

  <div class="hero-visual" role="img" aria-label="Dollar sign built from small social media icons over a faint grey icon collage"></div>

  <div class="section-head">
    <h2>What Is Bright Vellum</h2>
    <span class="rule"></span>
  </div>

  <section class="column col-one">
    <p>Based in Toronto with virtual offices across the globe, Bright Vellum is a niche Digital Media Agency with a focus on restaurants and nightlife. We are experts in customizing your operative social strategy to increase direct sales, traffic and brand awareness.</p>
    <p>Bright Vellum creates real world connections by merging the good old school handshake with a little modern day tool called The Internet. Our clients choose us because we listen to them and implement strategies that will turn their objectives into creative and measurable realties.</p>
  </section>
  <span class="divider divider-a"></span>

  <section class="column col-two">
    <p>What we can guarantee you is; Brand awareness, consistent message, increase in sales and repeat customers, enhanced customer service, competitive edge, cost effective strategies, exposure and connections to new client bases.</p>
    <p>Digital Media has taken a dominant role in our day to day activities, let us take advantage and expose you to your direct consumer base and expand your brand. We’ll show you how to creatively turn your business into a booming one, how to takeover untapped markets and confidently become an innovative leader in the hospitality industry.</p>
  </section>
  <span class="divider divider-b"></span>

  <span class="base-rule"></span>

  <footer class="contact">
    <span>info@brightvellum.ca</span>
    <span>www.brightvellum.ca</span>
    <span class="dot"></span><span class="dot"></span><span class="dot"></span><span class="dot"></span>
    <span>brightvellum</span>
    <span>416.555.0142</span>
  </footer>
</main>
</body>
</html>
```